Quorvane Capital Modern Business Card

We need a modern business card template designed for Quorvane Capital.
Quorvane Capital is a diversified global cryptocurrency investment fund.

The font under the logo: Hiragino Kaku Gothic Pro

Color Hexcode: Main colors white (ffffff) & teal (188383), we are open to adding #fcca46 as an accent

Target Market(s)

Accredited Investors, high net worth individuals and institutional investors

Industry/Entity Type

Investment

Contact Information for Business Card

Contact Information should contain
Name
main phone +1 720 555 0147
cell
email

Font styles to use
Sans Serif
Other font styles liked:
• Hiragino Kaku Gothic Pro

Requirements
Must have
• would like to have icons that identify the contact information
• include our website: www.quorvanecapital.example
• include our Tagline: Diversified Crypto Investment Funds
Nice to have
• Would like to have a simple back side with the logo (without the words) and plenty of space

```html
<!DOCTYPE html>
<html lang="en">
<head>
<meta charset="utf-8">
<title>Quorvane Capital – Business Card</title>
<link rel="stylesheet" href="https://fonts.googleapis.com/css2?family=Arimo&family=Jost:wght@400;500&display=swap">
<style>
  :root {
    --teal: #1a9292;
    --white: #ffffff;
    --ink: #1a1a1a;
    --accent: #fcca46;
    --backdrop: #eceeed;
  }
  * { margin: 0; padding: 0; box-sizing: border-box; }
  html, body { width: 1200px; height: 1200px; overflow: hidden; }
  body { background: var(--backdrop); position: relative; font-family: "Jost", sans-serif; }

  .card {
    position: absolute;
    top: 276px;
    width: 358px;
    height: 628px;
    border-radius: 14px;
  }
  .card--front { left: 198px; background: var(--white); }
  .card--back { left: 633px; background: var(--teal); color: var(--white); }

  .brand-mark {
    position: absolute;
    left: 124px;
    top: 248px;
    width: 110px;
    height: 110px;
    border-radius: 50%;
    background: var(--teal);
  }
  .brand-name {
    position: absolute;
    left: 0; right: 0;
    top: 380px;
    text-align: center;
    font-family: "Arimo", sans-serif;
    font-size: 21px;
    letter-spacing: 0.2px;
    color: var(--ink);
    text-transform: uppercase;
  }
  .tagline {
    position: absolute;
    left: 0; right: 0;
    top: 528px;
    text-align: center;
    font-size: 15px;
    line-height: 19px;
    color: var(--teal);
    text-transform: uppercase;
  }
  .tagline-rule {
    position: absolute;
    left: 107px;
    top: 569px;
    width: 145px;
    height: 1.5px;
    background: var(--accent);
  }
  .website {
    position: absolute;
    left: 0; right: 0;
    top: 575px;
    text-align: center;
    font-size: 17px;
    color: var(--teal);
  }

  .person {
    position: absolute;
    left: 42px;
    top: 42px;
  }
  .person-name { font-size: 19px; line-height: 22px; text-transform: uppercase; }
  .person-title { font-size: 14.5px; line-height: 18px; }

  .contact {
    position: absolute;
    left: 42px;
    top: 472px;
    list-style: none;
    font-size: 19px;
    line-height: 24.5px;
  }
  .contact li { position: relative; }
  .contact-icon {
    position: absolute;
    left: -24px;
    top: 5px;
    width: 14px;
    height: 14px;
    fill: none;
    stroke: var(--white);
    stroke-width: 1.6;
    stroke-linecap: round;
    stroke-linejoin: round;
  }
</style>
</head>
<body>
  <section class="card card--front" aria-label="Card front">
    <div class="brand-mark" aria-hidden="true"></div>
    <p class="brand-name">Quorvane Capital</p>
    <p class="tagline">Diversified Crypto<br>Investment Funds</p>
    <div class="tagline-rule"></div>
    <p class="website">www.quorvanecapital.example</p>
  </section>

  <section class="card card--back" aria-label="Card back">
    <div class="person">
      <p class="person-name">Daniel Marsh</p>
      <p class="person-title">Chief Executive Officer</p>
    </div>
    <ul class="contact">
      <li>
        <svg class="contact-icon" viewBox="0 0 14 14" aria-hidden="true"><path d="M7 13s4.5-4.6 4.5-7.6a4.5 4.5 0 0 0-9 0C2.5 8.4 7 13 7 13z"/><circle cx="7" cy="5.4" r="1.6"/></svg>
        418 Alder Crest Way
      </li>
      <li>Pasadena, CA</li>
      <li>
        <svg class="contact-icon" viewBox="0 0 14 14" aria-hidden="true"><path d="M3 1.5h2.3l1.1 3-1.5 1a7 7 0 0 0 3.6 3.6l1-1.5 3 1.1V11a1.5 1.5 0 0 1-1.6 1.5A10.5 10.5 0 0 1 1.5 3.1 1.5 1.5 0 0 1 3 1.5z"/></svg>
        +1 720 555 0147
      </li>
      <li>
        <svg class="contact-icon" viewBox="0 0 14 14" aria-hidden="true"><rect x="3.5" y="1" width="7" height="12" rx="1.3"/><path d="M6.2 10.8h1.6"/></svg>
        843-555-0132
      </li>
      <li>
        <svg class="contact-icon" viewBox="0 0 14 14" aria-hidden="true"><rect x="1" y="2.8" width="12" height="8.4" rx="1"/><path d="M1.5 3.5 7 7.8l5.5-4.3"/></svg>
        marsh@quorvanecapital.example
      </li>
    </ul>
  </section>
</body>
</html>
```